KM PowerPoint Design

I need a slick PowerPoint template following my newly designed logo (see the attached ZIP file for logo details, fonts, and colors).
Please also see the Sample.pptx file for an idea of the simplicity and slickness I am after (do not consider the colors or fonts from the Sample file, just as an idea). Other ideas are very welcome.

```html
<!DOCTYPE html>
<html lang="en">
<head>
<meta charset="utf-8">
<title>KM Presentation Template</title>
<link href="https://fonts.googleapis.com/css2?family=Poppins:ital,wght@0,400;0,500;0,600;0,700;0,800;1,500&display=swap" rel="stylesheet">
<style>
:root{
  --navy:#0b0f6e;
  --blue:#1f2fb0;
  --grad:linear-gradient(135deg,#0a0d66 0%,#2233b8 100%);
  --ink:#1b1d33;
  --muted:#8b8fa2;
  --grey:#b9bcc6;
  --paper:#ffffff;
  --stage:#dcdee3;
}
*{margin:0;padding:0;box-sizing:border-box}
html,body{width:1025px;height:1200px;overflow:hidden}
body{background:linear-gradient(180deg,#e2e3e7,#d6d8de);font-family:"Poppins",sans-serif;color:var(--ink);position:relative}
.slide{position:absolute;width:301px;height:170px;background:var(--paper);overflow:hidden;box-shadow:0 2px 5px rgba(0,0,0,.22)}
.c1{left:45px}.c2{left:362px}.c3{left:679px}
.r1{top:53px}.r2{top:238px}.r3{top:422px}.r4{top:607px}.r5{top:790px}.r6{top:973px}
.abs{position:absolute}
.fill{background:var(--grad)}
.photo{position:absolute}
.pg{position:absolute;right:9px;bottom:5px;font-size:4px;color:var(--ink)}
.h{font-weight:800;color:var(--navy);line-height:1.05}
.tiny{font-size:3.3px;line-height:1.45;color:var(--muted)}
.white{color:#fff}
.rule{position:absolute;height:1.5px;width:12px;background:var(--blue)}
.rule::after{content:"";position:absolute;left:14px;top:0;width:3px;height:1.5px;background:var(--blue);box-shadow:4px 0 0 var(--blue)}
.bar{position:absolute;width:5px;background:var(--grad)}
</style>
</head>
<body>

<!-- 1 Cover -->
<section class="slide c1 r1">
  <div class="abs" style="left:6px;top:6px;width:8px;height:8px;background:var(--navy)"></div>
  <div class="abs h" style="left:40px;top:30px;font-size:22px">KM</div>
  <div class="abs h" style="left:18px;top:76px;font-size:21px;color:var(--blue)">BUSINESS</div>
  <div class="abs" style="left:18px;top:102px;font-size:10px;font-weight:500;color:var(--navy)">MARKETING</div>
  <div class="rule" style="left:18px;top:120px"></div>
  <div class="abs" style="left:18px;top:124px;font-size:7px;font-style:italic;font-weight:500">Presentation</div>
  <div class="abs tiny" style="left:18px;top:133px;width:85px;font-style:italic">Lorem ipsum dolor sit amet, consectetuer adipiscing elit, sed diam nonum</div>
  <div class="abs" style="left:18px;top:150px;font-size:9px;color:var(--blue);letter-spacing:1px">&#8226;&#8226;&#8226;</div>
  <div class="photo" role="img" aria-label="Students working together at computers" style="left:127px;top:0;width:174px;height:136px;background:linear-gradient(135deg,#9aa3b5,#6c7386 55%,#b8bcc6)"></div>
  <div class="abs fill" style="left:127px;top:136px;width:174px;height:34px"></div>
  <div class="abs white" style="left:127px;top:149px;width:174px;text-align:center;font-size:5.5px;letter-spacing:2.4px">WWW.KMSTUDIO.CO</div>
</section>

<!-- 2 Agenda -->
<section class="slide c2 r1">
  <div class="photo" role="img" aria-label="Team meeting in a bright office" style="left:40px;top:0;width:106px;height:170px;background:linear-gradient(160deg,#e3e8ef,#9ea9b8 60%,#c9cfd8)"></div>
  <div class="abs fill" style="left:25px;top:25px;width:32px;height:121px"></div>
  <div class="abs white" style="left:25px;top:25px;width:32px;height:121px;writing-mode:vertical-rl;display:flex;align-items:center;justify-content:center;font-size:15px;font-weight:800">Agenda</div>
  <div class="abs" style="left:161px;top:36px;width:120px">
    <div style="font-size:5.5px;font-weight:600;color:var(--blue)">1. Lorem ipsum</div>
    <div class="tiny" style="margin:1px 0 15px">Lorem ipsum dolor sit amet, consectetuer adipiscing elit, sed diam nonummy nibh euismod tincid</div>
    <div style="font-size:5.5px;font-weight:600;color:var(--blue)">2. Lorem ipsum</div>
    <div class="tiny" style="margin:1px 0 15px">Lorem ipsum dolor sit amet, consectetuer adipiscing elit, sed diam nonummy nibh euismod tincid</div>
    <div style="font-size:5.5px;font-weight:600;color:var(--blue)">3. Lorem ipsum</div>
    <div class="tiny" style="margin:1px 0 14px">Lorem ipsum dolor sit amet, consectetuer adipiscing elit, sed diam nonummy nibh euismod tincid</div>
    <div style="font-size:5.5px;font-weight:600;color:var(--blue)">4. Lorem ipsum</div>
    <div class="tiny" style="margin-top:1px">Lorem ipsum dolor sit amet, consectetuer adipiscing elit, sed diam nonummy nibh euismod tincid</div>
  </div>
  <div class="bar" style="left:297px;top:28px;width:4px;height:98px"></div>
  <div class="pg">2</div>
</section>

<!-- 3 Education -->
<section class="slide c3 r1">
  <div class="bar" style="left:0;top:46px;width:10px;height:84px"></div>
  <div class="abs h" style="left:16px;top:53px;font-size:18.5px;color:var(--blue)">Text<br>Added<br>Here</div>
  <div class="photo" role="img" aria-label="Students around an education themed table" style="left:96px;top:28px;width:205px;height:82px;background:linear-gradient(135deg,#8e96a6,#c7ccd6 55%,#a7b0c2)"></div>
  <div class="abs" style="left:134px;top:80px;width:58px;height:73px;background:#fff;box-shadow:0 1px 3px rgba(0,0,0,.15)">
    <div class="fill white" style="height:20px;font-size:9px;font-weight:700;text-align:center;line-height:20px">Text Here</div>
    <div class="tiny" style="padding:3px 5px">Lorem ipsum dolor sit amet, consectetuer adipiscing elit, sed diam nonummy nibh euismod tincidunt ut laoreet dolore magna.<br><br>Ut wisi enim ad minim veniam, quis nostrud exerci tation ullamcorper suscipit lobortis nisl.</div>
  </div>
  <div class="abs" style="left:210px;top:80px;width:59px;height:73px;background:#fff;box-shadow:0 1px 3px rgba(0,0,0,.15)">
    <div class="fill white" style="height:20px;font-size:9px;font-weight:700;text-align:center;line-height:20px">Text Here</div>
    <div class="tiny" style="padding:3px 5px">Lorem ipsum dolor sit amet, consectetuer adipiscing elit, sed diam nonummy nibh euismod tincidunt ut laoreet dolore magna.<br><br>Ut wisi enim ad minim veniam, quis nostrud exerci tation ullamcorper suscipit lobortis nisl.</div>
  </div>
  <div class="pg">3</div>
</section>

<!-- 4 Graduation -->
<section class="slide c1 r2">
  <div class="bar" style="left:0;top:0;width:8px;height:170px"></div>
  <div class="abs fill" style="left:236px;top:0;width:65px;height:63px"></div>
  <div class="abs fill" style="left:149px;top:101px;width:76px;height:69px"></div>
  <div class="photo" role="img" aria-label="Graduates throwing caps into the sky" style="left:146px;top:31px;width:135px;height:108px;background:linear-gradient(180deg,#c9d6e6,#7c879b 60%,#3c4258)"></div>
  <div class="abs h" style="left:28px;top:35px;font-size:10px">Lorem Ipsum<br>Dolor Sit<br>Ametkeeper.</div>
  <div class="rule" style="left:28px;top:76px"></div>
  <div class="abs tiny" style="left:28px;top:81px;width:95px">Lorem ipsum dolor sit amet, consectetuer adipiscing elit, sed diam nonummy nibh euismod tincidunt ut laoreet dolore magna aliquam erat volutpat. Ut wisi enim ad minim veniam, quis nostrud exerci tation.<br><br>Lorem ipsum dolor sit amet, cons ectetuer adipiscing elit, sed diam nonum ad minim veniam, quis nostrud exerci tation ullamcorper</div>
  <div class="pg">4</div>
</section>

<!-- 5 Part One -->
<section class="slide c2 r2">
  <div class="bar" style="left:0;top:0;width:8px;height:170px"></div>
  <div class="photo" role="img" aria-label="Two colleagues looking at a tablet" style="left:164px;top:15px;width:117px;height:139px;background:linear-gradient(160deg,#dfe3ea,#9aa2b2 60%,#59617a)"></div>
  <div class="abs fill white" style="left:133px;top:51px;width:67px;height:67px;font-size:38px;font-weight:800;text-align:center;line-height:67px">01</div>
  <div class="abs h" style="left:27px;top:58px;font-size:14px">Part One</div>
  <div class="abs tiny" style="left:27px;top:77px;width:95px">Lorem ipsum dolor sit amet, laoreet dolore magna aliquam erat volutpat. Ut wisi it lob edo consequat. Duis autem lore te feugait nulla facilisi.<br><br>Lorem ipsum dolor sit amet, cons ectetuer adipiscing elit, sed diam nonum ad minim veniam, quis nostrud exerci tation ullamcorper</div>
  <div class="pg">5</div>
</section>

<!-- 6 Stats -->
<section class="slide c3 r2">
  <div class="bar" style="left:0;top:5px;width:10px;height:55px"></div>
  <div class="abs h" style="left:16px;top:12px;font-size:12.5px">Lorem<br>Dolor Sit<br>Consectetuer</div>
  <div class="abs" style="left:173px;top:36px;width:50px;text-align:center">
    <div style="font-size:9px;font-weight:800;color:var(--navy)">768K</div>
    <div style="font-size:5px;font-weight:600;color:var(--blue)">Lorem Ipsum</div>
    <div class="tiny">Lorem ipsum dolor sit amet, consectetuer elit.</div>
  </div>
  <div class="abs" style="left:239px;top:36px;width:50px;text-align:center">
    <div style="font-size:9px;font-weight:800;color:var(--navy)">423K</div>
    <div style="font-size:5px;font-weight:600;color:var(--blue)">Lorem Ipsum</div>
    <div class="tiny">Lorem ipsum dolor sit amet, consectetuer elit.</div>
  </div>
  <div class="abs tiny" style="left:16px;top:70px;width:118px">Lorem ipsum dolor sit amet, consectetuer adipiscing elit, sed diam nonummy nibh euismod tincidunt ut laoreet dolore magna aliquam erat volutpat. Ut wisi enim ad minim veniam, quis nostrud exerci tation ullamcorper suscipit</div>
  <div class="abs fill white" style="left:171px;top:90px;width:130px;height:21px;font-size:9px;font-weight:600;padding-left:9px;line-height:21px">Text Added Here</div>
  <div class="abs fill" style="left:67px;top:112px;width:234px;height:58px"></div>
  <div class="photo" role="img" aria-label="Presenter at a whiteboard with seated team" style="left:73px;top:112px;width:210px;height:58px;background:linear-gradient(135deg,#d5dae2,#8d95a7 55%,#c2c7d1)"></div>
  <div class="pg white">6</div>
</section>

<!-- 7 Bar chart -->
<section class="slide c1 r3">
  <div class="abs h" style="left:16px;top:12px;font-size:10px">Text<br>Added Hare</div>
  <div class="rule" style="left:16px;top:37px"></div>
  <div class="abs fill" style="left:0;top:51px;width:97px;height:101px"></div>
  <div class="abs white" style="left:16px;top:59px;width:78px">
    <div style="position:relative;padding-left:17px;margin-bottom:8px"><span style="position:absolute;left:0;top:0;width:12px;height:12px;background:#fff;color:var(--navy);font-size:7px;font-weight:800;text-align:center;line-height:12px">1.</span><div style="font-size:5px;font-weight:600">Lorem ipsum</div><div style="font-size:3.2px;line-height:1.35">Lorem ipsum dolor sit amet, consectetuer adipiscing elit, sed diam nonummy nibh euismod tincid</div></div>
    <div style="position:relative;padding-left:17px;margin-bottom:8px"><span style="position:absolute;left:0;top:0;width:12px;height:12px;background:#fff;color:var(--navy);font-size:7px;font-weight:800;text-align:center;line-height:12px">2.</span><div style="font-size:5px;font-weight:600">Lorem ipsum</div><div style="font-size:3.2px;line-height:1.35">Lorem ipsum dolor sit amet, consectetuer adipiscing elit, sed diam nonummy nibh euismod tincid</div></div>
    <div style="position:relative;padding-left:17px"><span style="position:absolute;left:0;top:0;width:12px;height:12px;background:#fff;color:var(--navy);font-size:7px;font-weight:800;text-align:center;line-height:12px">3.</span><div style="font-size:5px;font-weight:600">Lorem ipsum</div><div style="font-size:3.2px;line-height:1.35">Lorem ipsum dolor sit amet, consectetuer adipiscing elit, sed diam nonummy nibh euismod tincid</div></div>
  </div>
  <svg class="abs" style="left:103px;top:34px" width="190" height="115" viewBox="0 0 190 115" font-family="Poppins,sans-serif" font-size="3.6" fill="#444">
    <line x1="2" y1="90" x2="186" y2="90" stroke="#ccc" stroke-width=".4"/>
    <g>
      <rect x="18" y="38" width="4.5" height="52" fill="#0b0f6e"/><rect x="24" y="61" width="4.5" height="29" fill="#1f2fb0"/><rect x="30" y="66" width="4.5" height="24" fill="#b9bcc6"/>
      <text x="16" y="36">43%</text><text x="22" y="59">24%</text><text x="30" y="64">20%</text><text x="22" y="97">1</text>
      <rect x="63" y="37" width="4.5" height="53" fill="#0b0f6e"/><rect x="69" y="20" width="4.5" height="70" fill="#1f2fb0"/><rect x="75" y="66" width="4.5" height="24" fill="#b9bcc6"/>
      <text x="61" y="35">25%</text><text x="66" y="18">44%</text><text x="75" y="64">20%</text><text x="67" y="97">2</text>
      <rect x="108" y="48" width="4.5" height="42" fill="#0b0f6e"/><rect x="114" y="68" width="4.5" height="22" fill="#1f2fb0"/><rect x="120" y="54" width="4.5" height="36" fill="#b9bcc6"/>
      <text x="106" y="46">35%</text><text x="112" y="66">18%</text><text x="119" y="52">30%</text><text x="112" y="97">3</text>
      <rect x="153" y="36" width="4.5" height="54" fill="#0b0f6e"/><rect x="159" y="56" width="4.5" height="34" fill="#1f2fb0"/><rect x="165" y="30" width="4.5" height="60" fill="#b9bcc6"/>
      <text x="151" y="16">45%</text><text x="157" y="54">28%</text><text x="163" y="10">50%</text><text x="157" y="97">4</text>
    </g>
    <rect x="59" y="104" width="2" height="2" fill="#0b0f6e"/><text x="62" y="106">Series1</text>
    <rect x="77" y="104" width="2" height="2" fill="#1f2fb0"/><text x="80" y="106">Series2</text>
    <rect x="95" y="104" width="2" height="2" fill="#b9bcc6"/><text x="98" y="106">Series3</text>
  </svg>
  <div class="pg">7</div>
</section>

<!-- 8 Donuts -->
<section class="slide c2 r3">
  <div class="bar" style="left:0;top:21px;width:5px;height:127px"></div>
  <div class="abs h" style="left:0;top:12px;width:301px;text-align:center;font-size:10px">Text Added Hare</div>
  <div class="rule" style="left:141px;top:27px"></div>
  <div class="abs tiny" style="left:55px;top:37px;width:190px;text-align:center">Lorem ipsum dolor sit amet, consectetuer adipiscing elit, sed diam nonummy nibh euismod tincidunt ut laoreet dolore magna aliquam erat volutpat. Ut wisi enim ad minim veniam, quis nostrud exerci tation ullamcorper suscipit lobortis nisl ut aliquip ex ea commodo consequat. Duis autem vel eum iriure</div>
  <svg class="abs" style="left:0;top:66px" width="301" height="80" viewBox="0 0 301 80" font-family="Poppins,sans-serif">
    <g transform="translate(73,30)"><circle r="25" fill="none" stroke="#eceef2" stroke-width="4"/><circle r="25" fill="none" stroke="#0b0f6e" stroke-width="4" stroke-dasharray="78.5 157" transform="rotate(-90)"/><text text-anchor="middle" y="5" font-size="13" font-weight="600" fill="#1b1d33">50%</text></g>
    <g transform="translate(150,30)"><circle r="25" fill="none" stroke="#eceef2" stroke-width="4"/><circle r="25" fill="none" stroke="#1f2fb0" stroke-width="4" stroke-dasharray="117.8 157" transform="rotate(-90)"/><text text-anchor="middle" y="5" font-size="13" font-weight="600" fill="#1b1d33">75%</text></g>
    <g transform="translate(228,30)"><circle r="25" fill="none" stroke="#eceef2" stroke-width="4"/><circle r="25" fill="none" stroke="#b9bcc6" stroke-width="4" stroke-dasharray="62.8 157" transform="rotate(-90)"/><text text-anchor="middle" y="5" font-size="13" font-weight="600" fill="#1b1d33">40%</text></g>
    <g font-size="3.6" fill="#8b8fa2" text-anchor="middle"><text x="73" y="66">Lorem ipsum dolor amet amet</text><text x="73" y="71">consectetur dolor</text><text x="150" y="66">Lorem ipsum dolor amet amet</text><text x="150" y="71">consectetur dolor</text><text x="228" y="66">Lorem ipsum dolor amet amet</text><text x="228" y="71">consectetur dolor</text></g>
  </svg>
  <div class="pg">8</div>
</section>

<!-- 9 Cycle -->
<section class="slide c3 r3">
  <div class="abs h" style="left:16px;top:12px;font-size:10px">Text<br>Added Hare</div>
  <div class="rule" style="left:16px;top:37px"></div>
  <div class="abs tiny" style="left:16px;top:49px;width:90px">Lorem ipsum dolor sit amet, consectetuer adipiscing elit, sed diam nonummy nibh.<br><br>Ut wisi enim ad minim veniam, quis nostrud exerci tation ullamcorper suscipit lobortis. Ut wisi enim ad minim veniam, quis nostrud exerci tation.</div>
  <div class="abs fill white" style="left:0;top:96px;width:97px;height:56px;padding:6px 6px 0 16px">
    <div style="font-size:5px;font-weight:600">Lorem ipsum</div><div style="font-size:3.1px;line-height:1.35;margin-bottom:5px">Lorem ipsum dolor sit amet, consectetuer adipiscing elit, sed diam nonummy nibh euismod tincidunt ut laoreet</div>
    <div style="font-size:5px;font-weight:600">Lorem ipsum</div><div style="font-size:3.1px;line-height:1.35">Lorem ipsum dolor sit amet, consectetuer adipiscing elit, sed diam nonummy nibh euismod tincidunt ut laoreet</div>
  </div>
  <div class="abs" style="left:7px;top:101px;width:4px;height:4px;border-radius:50%;background:#fff"></div>
  <div class="abs" style="left:7px;top:126px;width:4px;height:4px;border-radius:50%;background:#fff"></div>
  <div class="bar" style="left:295px;top:21px;width:6px;height:127px"></div>
  <svg class="abs" style="left:100px;top:25px" width="195" height="145" viewBox="0 0 195 145" font-family="Poppins,sans-serif">
    <path d="M128 14 A52 52 0 1 0 98 108" fill="none" stroke="#0b0f6e" stroke-width="2"/>
    <path d="M35 60 L38 72 L44 62" fill="none" stroke="#0b0f6e" stroke-width="2"/>
    <path d="M53 94 L56 96" stroke="#0b0f6e" stroke-width="2"/>
    <circle cx="128" cy="28" r="18" fill="#1f2fb0"/><circle cx="128" cy="28" r="13" fill="none" stroke="#fff" stroke-width="1.2"/><circle cx="128" cy="27" r="4" fill="none" stroke="#fff" stroke-width="1.2"/><line x1="125" y1="30" x2="122" y2="33" stroke="#fff" stroke-width="1.2"/>
    <circle cx="139" cy="73" r="12" fill="#1f2fb0"/><circle cx="139" cy="73" r="8" fill="none" stroke="#fff" stroke-width="1"/><circle cx="139" cy="72" r="2.5" fill="#fff"/>
    <circle cx="114" cy="104" r="10" fill="#1f2fb0"/><circle cx="114" cy="104" r="6.5" fill="none" stroke="#fff" stroke-width="1"/><line x1="114" y1="100" x2="114" y2="107" stroke="#fff"/>
    <circle cx="53" cy="94" r="9" fill="#1f2fb0"/><circle cx="53" cy="94" r="6" fill="none" stroke="#fff" stroke-width="1"/><circle cx="53" cy="94" r="1.5" fill="#fff"/>
    <circle cx="40" cy="86" r="3" fill="#0b0f6e"/>
    <rect x="67" y="34" width="2" height="8" fill="#0b0f6e"/><rect x="70" y="37" width="2" height="5" fill="#0b0f6e"/><rect x="73" y="32" width="2" height="10" fill="#0b0f6e"/><rect x="66" y="42" width="11" height="1" fill="#0b0f6e"/>
    <text x="71" y="51" text-anchor="middle" font-size="4.5" font-weight="600" fill="#1b1d33">MAIN TITLE</text>
    <text x="71" y="56" text-anchor="middle" font-size="2.6" fill="#8b8fa2">Lorem ipsum dolor sit amet</text><text x="71" y="59" text-anchor="middle" font-size="2.6" fill="#8b8fa2">consectetuer adipiscing elit</text>
    <g font-size="3" font-weight="700" font-style="italic" fill="#0b0f6e"><text x="147" y="14">85%</text><text x="118" y="72">80%</text><text x="72" y="92">50%</text><text x="130" y="121">75%</text></g>
    <g font-size="4.3" font-weight="600" fill="#1b1d33"><text x="150" y="30">Your Title</text><text x="157" y="69">Your Title</text><text x="141" y="107">Your Title</text><text x="5" y="92">Your Title</text></g>
    <g font-size="2.4" fill="#8b8fa2"><text x="150" y="35">Lorem ipsum dolor sit amet,</text><text x="150" y="38">sed diam nonummy nibh</text><text x="157" y="74">Lorem ipsum dolor sit amet,</text><text x="157" y="77">sed diam nonummy nibh</text><text x="141" y="112">Lorem ipsum dolor sit amet,</text><text x="141" y="115">sed diam nonummy nibh</text><text x="5" y="97">Lorem ipsum dolor sit amet,</text><text x="5" y="100">sed diam nonummy nibh</text></g>
  </svg>
  <div class="pg">9</div>
</section>

<!-- 10 Service -->
<section class="slide c1 r4">
  <div class="abs fill" style="left:0;top:0;width:53px;height:36px"></div>
  <div class="photo" role="img" aria-label="Stack of books with a diploma and graduation cap" style="left:19px;top:18px;width:113px;height:133px;background:linear-gradient(170deg,#3e4148,#8a8c92 55%,#d8d8da)"></div>
  <div class="abs fill white" style="left:42px;top:131px;width:67px;height:20px;font-size:10px;font-weight:700;text-align:center;line-height:20px">Service</div>
  <div class="bar" style="left:295px;top:18px;width:6px;height:130px"></div>
  <div class="abs" style="left:147px;top:31px;width:145px">
    <div style="position:relative;padding-left:31px;height:43px"><svg style="position:absolute;left:0;top:0" width="24" height="24"><circle cx="12" cy="12" r="12" fill="#1f2fb0"/><circle cx="12" cy="12" r="7" fill="none" stroke="#fff"/><circle cx="12" cy="12" r="3.5" fill="none" stroke="#fff"/><line x1="12" y1="12" x2="19" y2="6" stroke="#fff"/></svg><div style="font-size:6px;font-weight:600;color:var(--blue)">Project name</div><div class="tiny">Lorem ipsum dolor sit amet, nec an dictas equidem appellantur. ut has commune accommodare. Mea illum. ludus solet idpro.</div></div>
    <div style="position:relative;padding-left:31px;height:44px"><svg style="position:absolute;left:0;top:0" width="24" height="24"><circle cx="12" cy="12" r="12" fill="#1f2fb0"/><circle cx="12" cy="12" r="7" fill="none" stroke="#fff"/><circle cx="12" cy="12" r="3.5" fill="none" stroke="#fff"/><line x1="12" y1="12" x2="19" y2="6" stroke="#fff"/></svg><div style="font-size:6px;font-weight:600;color:var(--blue)">Project name</div><div class="tiny">Lorem ipsum dolor sit amet, nec an dictas equidem appellantur. ut has commune accommodare. Mea illum. ludus solet idpro.</div></div>
    <div style="position:relative;padding-left:31px"><svg style="position:absolute;left:0;top:0" width="24" height="24"><circle cx="12" cy="12" r="12" fill="#1f2fb0"/><circle cx="12" cy="12" r="7" fill="none" stroke="#fff"/><circle cx="12" cy="12" r="3.5" fill="none" stroke="#fff"/><line x1="12" y1="12" x2="19" y2="6" stroke="#fff"/></svg><div style="font-size:6px;font-weight:600;color:var(--blue)">Project name</div><div class="tiny">Lorem ipsum dolor sit amet, nec an dictas equidem appellantur. ut has commune accommodare. Mea illum. ludus solet idpro.</div></div>
  </div>
  <div class="pg">10</div>
</section>

<!-- 11 SWOT -->
<section class="slide c2 r4">
  <div class="abs h" style="left:13px;top:9px;font-size:10px">Text Added Hare</div>
  <div class="rule" style="left:13px;top:25px"></div>
  <div class="bar" style="left:297px;top:18px;width:4px;height:130px"></div>
  <svg class="abs" style="left:0;top:0" width="301" height="170" viewBox="0 0 301 170" font-family="Poppins,sans-serif">
    <line x1="152" y1="38" x2="152" y2="143" stroke="#9aa0b4" stroke-width=".7" stroke-dasharray="1 1.5"/>
    <line x1="95" y1="90" x2="210" y2="90" stroke="#9aa0b4" stroke-width=".7" stroke-dasharray="1 1.5"/>
    <g fill="#1f2fb0"><circle cx="129" cy="67" r="20"/><circle cx="175" cy="67" r="20"/><circle cx="129" cy="114" r="20"/><circle cx="175" cy="114" r="20"/></g>
    <g fill="#fff" font-size="18" font-weight="600" text-anchor="middle"><text x="129" y="73">S</text><text x="175" y="73">W</text><text x="129" y="120">O</text><text x="175" y="120">T</text></g>
    <circle cx="152" cy="90" r="17" fill="#0b0f6e" stroke="#fff" stroke-width="1.5"/>
    <text x="152" y="92" text-anchor="middle" font-size="5" font-style="italic" font-weight="600" fill="#fff">ANALYSIS</text>
    <g font-size="4" font-weight="700" font-style="italic" fill="#1f2fb0"><text x="74" y="44">STRENGTHS</text><text x="197" y="42">WEAKNESSES</text><text x="71" y="107">OPPORTUNITIES</text><text x="201" y="104">THREATS</text></g>
    <g font-size="2.4" fill="#8b8fa2">
      <text x="77" y="49">• Good location</text><text x="77" y="55">• Very affordable prices</text><text x="77" y="61">• Variety of activities</text><text x="77" y="67">• Personal trainer</text>
      <text x="199" y="48">• Not many promotions</text><text x="200" y="51">during the year</text><text x="199" y="57">• Small fitness</text><text x="200" y="60">training rooms</text><text x="199" y="66">• Presence in social</text><text x="200" y="69">networks can</text><text x="200" y="72">be improved</text>
      <text x="73" y="112">• Hiring more graphic</text><text x="74" y="115">designers and</text><text x="74" y="118">marketing members</text><text x="73" y="124">• An app can be practical</text><text x="74" y="127">to track results, find</text><text x="74" y="130">information about</text><text x="74" y="133">workout statistics</text>
      <text x="203" y="109">• Others gyms have more</text><text x="204" y="112">space to workout and</text><text x="204" y="115">running clubs</text><text x="203" y="121">• There are many free</text><text x="204" y="124">fitness app</text><text x="203" y="130">• Principal competitors</text><text x="204" y="133">have nutritionist</text>
    </g>
  </svg>
  <div class="pg">11</div>
</section>

<!-- 12 Hub -->
<section class="slide c3 r4">
  <div class="bar" style="left:0;top:18px;width:5px;height:133px"></div>
  <svg class="abs" style="left:0;top:0" width="301" height="170" viewBox="0 0 301 170" font-family="Poppins,sans-serif">
    <circle cx="66" cy="83" r="40" fill="none" stroke="#0b0f6e" stroke-width="2"/>
    <circle cx="66" cy="83" r="35" fill="#1f2fb0"/>
    <text x="66" y="75" text-anchor="middle" font-size="11" font-weight="700" fill="#fff">Text</text>
    <text x="66" y="88" text-anchor="middle" font-size="11" font-weight="700" fill="#fff">Added</text>
    <text x="66" y="101" text-anchor="middle" font-size="11" font-weight="700" fill="#fff">Hare</text>
    <g stroke="#555" stroke-width=".5" fill="none"><path d="M106 58 L122 43 L148 43"/><path d="M113 83 L148 83"/><path d="M106 108 L122 125 L148 125"/></g>
  </svg>
  <div class="abs" style="left:154px;top:31px;width:140px">
    <div style="position:relative;padding-left:33px;height:42px"><svg style="position:absolute;left:0;top:0" width="26" height="26"><circle cx="13" cy="13" r="13" fill="#1f2fb0"/><circle cx="13" cy="13" r="7.5" fill="none" stroke="#fff"/><circle cx="13" cy="13" r="3.5" fill="none" stroke="#fff"/><line x1="13" y1="13" x2="20" y2="7" stroke="#fff"/></svg><div style="font-size:6px;font-weight:600;color:var(--blue)">Project name</div><div class="tiny">Lorem ipsum dolor sit amet, nec an dictas equidem appellantur. ut has commune accommodare. Mea illum. ludus solet idpro.</div></div>
    <div style="position:relative;padding-left:33px;height:42px"><svg style="position:absolute;left:0;top:0" width="26" height="26"><circle cx="13" cy="13" r="13" fill="#1f2fb0"/><circle cx="13" cy="13" r="7.5" fill="none" stroke="#fff"/><circle cx="13" cy="13" r="3.5" fill="none" stroke="#fff"/><line x1="13" y1="13" x2="20" y2="7" stroke="#fff"/></svg><div style="font-size:6px;font-weight:600;color:var(--blue)">Project name</div><div class="tiny">Lorem ipsum dolor sit amet, nec an dictas equidem appellantur. ut has commune accommodare. Mea illum. ludus solet idpro.</div></div>
    <div style="position:relative;padding-left:33px"><svg style="position:absolute;left:0;top:0" width="26" height="26"><circle cx="13" cy="13" r="13" fill="#1f2fb0"/><circle cx="13" cy="13" r="7.5" fill="none" stroke="#fff"/><circle cx="13" cy="13" r="3.5" fill="none" stroke="#fff"/><line x1="13" y1="13" x2="20" y2="7" stroke="#fff"/></svg><div style="font-size:6px;font-weight:600;color:var(--blue)">Project name</div><div class="tiny">Lorem ipsum dolor sit amet, nec an dictas equidem appellantur. ut has commune accommodare. Mea illum. ludus solet idpro.</div></div>
  </div>
  <div class="pg">12</div>
</section>

<!-- 13 Timeline -->
<section class="slide c1 r5">
  <div class="abs fill white" style="left:0;top:12px;width:157px;height:18px;font-size:10px;font-weight:700;padding-left:15px;line-height:18px">Project Timeline - 2024</div>
  <svg class="abs" style="left:0;top:0" width="301" height="170" viewBox="0 0 301 170" font-family="Poppins,sans-serif">
    <g fill="#0b0f6e">
      <polygon points="36,89 74,89 78,97 32,97"/><polygon points="81,89 118,89 123,97 77,97" fill="#1f2fb0"/><polygon points="126,89 163,89 168,97 122,97"/><polygon points="170,89 208,89 212,97 166,97" fill="#1f2fb0"/><polygon points="215,89 253,89 258,97 211,97"/>
    </g>
    <g font-size="4" font-weight="600" fill="#fff" text-anchor="middle"><text x="56" y="94.5">1990</text><text x="100" y="94.5">2001</text><text x="145" y="94.5">2007</text><text x="189" y="94.5">2012</text><text x="234" y="94.5">2020</text></g>
    <g stroke="#0b0f6e" stroke-width=".8"><line x1="56" y1="75" x2="56" y2="88"/><line x1="145" y1="75" x2="145" y2="88"/><line x1="234" y1="75" x2="234" y2="88"/><line x1="100" y1="98" x2="100" y2="109"/><line x1="189" y1="98" x2="189" y2="109"/></g>
    <g fill="#0b0f6e"><circle cx="56" cy="75" r="1.8"/><circle cx="145" cy="75" r="1.8"/><circle cx="234" cy="75" r="1.8"/><circle cx="100" cy="109" r="1.8"/><circle cx="189" cy="109" r="1.8"/></g>
    <g text-anchor="middle"><g font-size="4.5" font-weight="600" fill="#1f2fb0"><text x="56" y="58">Your Title</text><text x="145" y="58">Your Title</text><text x="234" y="58">Your Title</text><text x="100" y="125">Your Title</text><text x="189" y="125">Your Title</text></g>
    <g font-size="3.4" fill="#8b8fa2"><text x="56" y="63">Refers to a good or</text><text x="56" y="67">service being offered</text><text x="145" y="63">Refers to a good or</text><text x="145" y="67">service being offered</text><text x="234" y="63">Refers to a good or</text><text x="234" y="67">service being offered</text><text x="100" y="130">Refers to a good or</text><text x="100" y="134">service being offered</text><text x="189" y="130">Refers to a good or</text><text x="189" y="134">service being offered</text></g></g>
  </svg>
  <div class="pg">13</div>
</section>

<!-- 14 List -->
<section class="slide c2 r5">
  <div class="abs fill" style="left:0;top:0;width:105px;height:170px"></div>
  <div class="abs white" style="left:18px;top:25px;width:28px;height:125px;writing-mode:vertical-rl;font-size:11px;font-weight:800;letter-spacing:3px;display:flex;align-items:center">TEXT ADDED</div>
  <div class="abs fill white" style="left:58px;top:27px;width:107px;height:30px;font-size:9.5px;font-weight:700;padding-left:14px;line-height:30px;box-shadow:0 1px 3px rgba(0,0,0,.3)">1. Lorem Ipsum</div>
  <div class="abs fill white" style="left:58px;top:70px;width:107px;height:31px;font-size:9.5px;font-weight:700;padding-left:14px;line-height:31px;box-shadow:0 1px 3px rgba(0,0,0,.3)">2. Lorem Ipsum</div>
  <div class="abs fill white" style="left:58px;top:120px;width:107px;height:31px;font-size:9.5px;font-weight:700;padding-left:14px;line-height:31px;box-shadow:0 1px 3px rgba(0,0,0,.3)">3. Lorem Ipsum</div>
  <div class="abs h" style="left:185px;top:49px;font-size:10px">Text<br>Added Hare</div>
  <div class="rule" style="left:185px;top:75px"></div>
  <div class="abs tiny" style="left:185px;top:82px;width:92px">Lorem ipsum dolor sit amet, consectetuer adipiscing elit, sed diam nonummy nibh.<br><br>Ut wisi enim ad minim veniam, quis nostrud exerci tation ullamcorper suscipit lobortis. Ut wisi enim ad minim veniam, quis nostrud exerci tation ullamcorper suscipit</div>
  <div class="pg">14</div>
</section>

<!-- 15 Steps -->
<section class="slide c3 r5">
  <div class="abs h" style="left:12px;top:9px;font-size:10px">Text Added Hare</div>
  <div class="rule" style="left:12px;top:25px"></div>
  <svg class="abs" style="left:0;top:0" width="301" height="170" viewBox="0 0 301 170" font-family="Poppins,sans-serif">
    <rect x="20" y="89" width="250" height="4" fill="#0b0f6e"/>
    <polygon points="268,86 277,91 268,96" fill="#1f2fb0"/>
    <g>
      <circle cx="69" cy="76" r="18" fill="#0b0f6e"/><circle cx="69" cy="76" r="12" fill="#fff"/><circle cx="69" cy="76" r="6" fill="none" stroke="#0b0f6e"/><path d="M69 72 V76 L72 78" stroke="#0b0f6e" fill="none"/>
      <circle cx="122" cy="76" r="18" fill="#1f2fb0"/><circle cx="122" cy="76" r="12" fill="#fff"/><circle cx="122" cy="76" r="6" fill="#0b0f6e"/><text x="122" y="78" text-anchor="middle" font-size="6" fill="#fff">$</text>
      <circle cx="175" cy="76" r="18" fill="#0b0f6e"/><circle cx="175" cy="76" r="12" fill="#fff"/><g fill="#0b0f6e"><rect x="170" y="71" width="10" height="2.5" rx="1"/><rect x="170" y="74.5" width="10" height="2.5" rx="1"/><rect x="170" y="78" width="10" height="2.5" rx="1"/></g>
      <circle cx="228" cy="76" r="18" fill="#1f2fb0"/><circle cx="228" cy="76" r="12" fill="#fff"/><circle cx="229" cy="75" r="3.5" fill="none" stroke="#0b0f6e"/><line x1="226.5" y1="77.5" x2="223.5" y2="80.5" stroke="#0b0f6e"/>
    </g>
    <g fill="#1f2fb0"><rect x="60" y="88" width="24" height="6" rx="1"/><rect x="113" y="88" width="24" height="6" rx="1"/><rect x="166" y="88" width="24" height="6" rx="1"/><rect x="219" y="88" width="24" height="6" rx="1"/></g>
    <g font-size="3.6" font-weight="600" fill="#fff" text-anchor="middle"><text x="72" y="92.3">Step 01</text><text x="125" y="92.3">Step 02</text><text x="178" y="92.3">Step 03</text><text x="231" y="92.3">Step 04</text></g>
    <g stroke="#8b8fa2" stroke-width=".6"><line x1="69" y1="96" x2="69" y2="104"/><line x1="122" y1="96" x2="122" y2="104"/><line x1="175" y1="96" x2="175" y2="104"/><line x1="228" y1="96" x2="228" y2="104"/></g>
    <g text-anchor="middle"><g font-size="5.5" font-weight="600" fill="#1b1d33"><text x="69" y="113">Lorem Ipsum</text><text x="122" y="113">Lorem Ipsum</text><text x="175" y="113">Lorem Ipsum</text><text x="228" y="113">Lorem Ipsum</text></g>
    <g font-size="2.5" fill="#8b8fa2"><text x="69" y="118">Lorem ipsum dolor sit amet,</text><text x="69" y="121">consectetuer adipiscing elit</text><text x="69" y="124">sed diam nonummy nibh</text><text x="122" y="118">Lorem ipsum dolor sit amet,</text><text x="122" y="121">consectetuer adipiscing elit</text><text x="122" y="124">sed diam nonummy nibh</text><text x="175" y="118">Lorem ipsum dolor sit amet,</text><text x="175" y="121">consectetuer adipiscing elit</text><text x="175" y="124">sed diam nonummy nibh</text><text x="228" y="118">Lorem ipsum dolor sit amet,</text><text x="228" y="121">consectetuer adipiscing elit</text><text x="228" y="124">sed diam nonummy nibh</text></g></g>
  </svg>
  <div class="pg">15</div>
</section>

<!-- 16 Devices -->
<section class="slide c1 r6">
  <div class="abs h" style="left:20px;top:18px;font-size:15px;color:var(--blue)">Text<br>Added<br>Here</div>
  <div class="abs fill white" style="left:0;top:87px;width:112px;height:66px;padding:6px 6px 0 19px">
    <div style="position:relative;height:20px"><span style="position:absolute;left:-13px;top:0;width:10px;height:10px;background:#fff;color:var(--navy);font-size:6px;font-weight:800;text-align:center;line-height:10px">1.</span><div style="font-size:5px;font-weight:600">Lorem Ipsum</div><div style="font-size:3px;line-height:1.3">Lorem ipsum dolor sit amet, consectetuer adipiscing elit, sed diam nonummy nibh euismod</div></div>
    <div style="position:relative;height:20px"><span style="position:absolute;left:-13px;top:0;width:10px;height:10px;background:#fff;color:var(--navy);font-size:6px;font-weight:800;text-align:center;line-height:10px">2.</span><div style="font-size:5px;font-weight:600">Lorem Ipsum</div><div style="font-size:3px;line-height:1.3">Lorem ipsum dolor sit amet, consectetuer adipiscing elit, sed diam nonummy nibh euismod</div></div>
    <div style="position:relative"><span style="position:absolute;left:-13px;top:0;width:10px;height:10px;background:#fff;color:var(--navy);font-size:6px;font-weight:800;text-align:center;line-height:10px">3.</span><div style="font-size:5px;font-weight:600">Lorem Ipsum</div><div style="font-size:3px;line-height:1.3">Lorem ipsum dolor sit amet, consectetuer adipiscing elit, sed diam nonummy nibh euismod</div></div>
  </div>
  <div class="photo" role="img" aria-label="Faint world map backdrop" style="left:120px;top:40px;width:175px;height:105px;background:radial-gradient(ellipse at center,#eef0f3,#ffffff 70%)"></div>
  <div class="abs" style="left:136px;top:26px;width:36px;height:75px;border:1.5px solid #222;border-radius:4px;background:#fff;padding:8px 3px">
    <div style="font-size:4px;font-weight:600;line-height:1.2">Lorem ipsum dolor</div>
    <div style="width:10px;height:8px;border:.8px solid var(--blue);margin:8px auto 6px"></div>
    <div style="font-size:2.4px;line-height:1.3;color:var(--muted)">To introduce the students to the changing landscape of marketing and equip them with knowledge and tools.</div>
  </div>
  <div class="abs" style="left:182px;top:49px;width:36px;height:75px;border:1.5px solid #222;border-radius:4px;background:#fff;padding:8px 3px">
    <div style="font-size:4px;font-weight:600;line-height:1.2">Dolor sit amet, conse</div>
    <div style="width:10px;height:8px;border:.8px solid var(--blue);margin:6px auto 6px"></div>
    <div style="font-size:2.4px;line-height:1.3;color:var(--muted)">You will learn concepts and ideas in digital marketing as well as how to use different tools and strategies.</div>
  </div>
  <div class="abs" style="left:227px;top:74px;width:36px;height:76px;border:1.5px solid #222;border-radius:4px;background:#fff;padding:8px 3px">
    <div style="font-size:4px;font-weight:600">Consec</div>
    <div style="font-size:4px;color:var(--blue);letter-spacing:1px">•••••</div>
    <div style="width:9px;height:9px;border:.8px solid var(--blue);border-radius:50%;margin:4px auto 5px"></div>
    <div style="font-size:2.4px;line-height:1.3;color:var(--muted)">You are required to pass 80% of the evaluation test to obtain the certificate.</div>
  </div>
  <div class="pg">22</div>
</section>

<!-- 17 Team -->
<section class="slide c2 r6">
  <div class="abs fill" style="left:0;top:19px;width:301px;height:59px"></div>
  <div class="abs white" style="left:0;top:34px;width:301px;text-align:center;font-size:13.5px;font-weight:700">The Team Members</div>
  <div class="abs" style="left:0;top:64px;width:301px;display:flex;justify-content:space-around;padding:0 20px">
    <div style="width:60px;text-align:center"><div role="img" aria-label="Team member portrait" style="width:26px;height:26px;margin:0 auto;border-radius:50%;border:1.5px solid #fff;background:linear-gradient(#c8cdd6,#8c93a3)"></div><div style="font-size:5px;font-weight:700;margin:5px 0 2px">OWEN HARTLEY</div><div class="tiny" style="font-size:2.6px">Lorem dolor sit amet, cons ectetuer adipiscing elit, sed diam nonummy nibh euismod tincidunt<br><br>ut laoreet dolore magna aliquam erat volutpat. Ut wisi enim ad minim veniam, quis nostrud</div></div>
    <div style="width:60px;text-align:center"><div role="img" aria-label="Team member portrait" style="width:26px;height:26px;margin:0 auto;border-radius:50%;border:1.5px solid #fff;background:linear-gradient(#c8cdd6,#8c93a3)"></div><div style="font-size:5px;font-weight:700;margin:5px 0 2px">NORA BELLAMY</div><div class="tiny" style="font-size:2.6px">Lorem dolor sit amet, cons ectetuer adipiscing elit, sed diam nonummy nibh euismod tincidunt<br><br>ut laoreet dolore magna aliquam erat volutpat. Ut wisi enim ad minim veniam, quis nostrud</div></div>
    <div style="width:60px;text-align:center"><div role="img" aria-label="Team member portrait" style="width:26px;height:26px;margin:0 auto;border-radius:50%;border:1.5px solid #fff;background:linear-gradient(#c8cdd6,#8c93a3)"></div><div style="font-size:5px;font-weight:700;margin:5px 0 2px">OWEN HARTLEY</div><div class="tiny" style="font-size:2.6px">Lorem dolor sit amet, cons ectetuer adipiscing elit, sed diam nonummy nibh euismod tincidunt<br><br>ut laoreet dolore magna aliquam erat volutpat. Ut wisi enim ad minim veniam, quis nostrud</div></div>
    <div style="width:60px;text-align:center"><div role="img" aria-label="Team member portrait" style="width:26px;height:26px;margin:0 auto;border-radius:50%;border:1.5px solid #fff;background:linear-gradient(#c8cdd6,#8c93a3)"></div><div style="font-size:5px;font-weight:700;margin:5px 0 2px">NORA BELLAMY</div><div class="tiny" style="font-size:2.6px">Lorem dolor sit amet, cons ectetuer adipiscing elit, sed diam nonummy nibh euismod tincidunt<br><br>ut laoreet dolore magna aliquam erat volutpat. Ut wisi enim ad minim veniam, quis nostrud</div></div>
  </div>
  <div class="pg">23</div>
</section>

<!-- 18 Thank you -->
<section class="slide c3 r6">
  <div class="abs" style="left:24px;top:30px;width:12px;height:12px;background:var(--navy)"></div>
  <div class="abs h" style="left:22px;top:48px;font-size:64px;letter-spacing:-2px">KM</div>
  <div class="abs h" style="left:177px;top:50px;font-size:19px;color:var(--ink)">Thank You</div>
  <svg class="abs" style="left:177px;top:82px" width="12" height="60" viewBox="0 0 12 60" fill="#1f2fb0">
    <path d="M2 3 C2 2 3 1 4 1 L5 1 L7 5 L5 6.5 C5.6 8 7 9.4 8.5 10 L10 8 L11.5 9.5 L11.5 11 C11.5 12 10.5 12.5 9.5 12.5 C5 12 2 8 2 3Z"/>
    <path d="M1 23 L11 27 L6.5 28.5 L5 33 Z"/>
    <path d="M6 42 L11.5 47 L10 47 L10 52 L7.5 52 L7.5 49 L4.5 49 L4.5 52 L2 52 L2 47 L0.5 47 Z"/>
  </svg>
  <div class="abs" style="left:192px;top:82px;width:1px;height:12px;background:var(--ink)"></div>
  <div class="abs" style="left:192px;top:104px;width:1px;height:12px;background:var(--ink)"></div>
  <div class="abs" style="left:192px;top:124px;width:1px;height:12px;background:var(--ink)"></div>
  <div class="abs" style="left:198px;top:82px;font-size:5px;line-height:1.3;color:#555">+18 2000 5550 1234<br>+18 2000 5550 1234</div>
  <div class="abs" style="left:198px;top:104px;font-size:5px;line-height:1.3;color:#555">www.kmstudio.co<br>hello@kmstudio.co</div>
  <div class="abs" style="left:198px;top:124px;font-size:5px;line-height:1.3;color:#555">1234 Street name, town/city,<br>state/country, post/zip 012345.</div>
</section>

</body>
</html>
```